Boutique Shoe Bag Race wear Business Card Design

We are a new luxury shoe bag, jewellery and race wear store stocking local and international designers. Located in the fashion precinct of beautiful Calloway Cove famous in Sydney Australia. Stocking French jewellery and shoes such as Renaud valmiers plus Australian made. Looking at quality and service and looking after the locals and tourists.
Ideas: White background, Black writing in bold engravers, logo in middle of Marlow and Boutique a gold horseshoe (facing upright so the curve is at the bottom) with a black stiletto inside. French clover silver and black border (not irish clover the French lattice type look)
Updates

Marlow Atelier

I open 8/4 so require business card design ASAP.

Please place gold horseshoe facing upwards with the black stiletto inside.

Bold engravers writing for business name.

I will have my phone number tomorrow to update.

Border in similar/same style as attached picture with black/silver clover French design.

Thank you. Tessa                                   

Industry/Entity Type

Fashion

Contact Information for Business Card

Marlow Atelier
Boutique Owner Tessa Wrenfield
41B Parrin Lane
Calloway Cove NSW 2093 Australia
0471239046
02 **** *TBA
info@marlowatelier.com.au
Facebook.com/MarlowAtelier
www.marlowatelier.com.au

Font styles to use
Other font styles liked:
• Bold Engravers

Requirements
Must have
• Info on one side including business name and logo with black stiletto and gold horse shoe. reverse side with French clover border and Larger name Marlow Atelier with logo in centre.
Should not have
• irish clover
French script
horseshoe upside down

```html
<!DOCTYPE html>
<html lang="en">
<head>
<meta charset="utf-8">
<title>Marlow Atelier — Business Card</title>
<link rel="stylesheet" href="https://fonts.googleapis.com/css2?family=Cinzel:wght@700&family=Marcellus&display=swap">
<style>
  :root {
    --backdrop: #e9e9e9;
    --card: #ffffff;
    --lattice: #6f6f6f;
    --lattice-dark: #2a2a2a;
    --ink: #111111;
    --muted: #5c5c5c;
    --gold: #c9a43a;
  }
  * { margin: 0; padding: 0; box-sizing: border-box; }
  html, body { width: 1200px; height: 1000px; overflow: hidden; }
  body { background: var(--backdrop); position: relative; font-family: "Marcellus", serif; }

  .card { position: absolute; background: var(--card); }
  .card--front { left: 334px; top: 130px; width: 555px; height: 342px; }
  .card--back  { left: 335px; top: 511px; width: 555px; height: 343px; }

  .lattice-border {
    position: absolute; inset: 0;
    background: radial-gradient(circle at 50% 50%, var(--lattice) 0%, #5a5a5a 100%);
  }
  .front-panel {
    position: absolute; left: 33px; top: 39px; width: 489px; height: 265px;
    background: var(--card);
  }

  .wordmark {
    position: absolute; left: 0; right: 0;
    display: flex; align-items: center; justify-content: center; gap: 14px;
    font-family: "Cinzel", serif; font-weight: 700; color: var(--ink);
    letter-spacing: 0.08em; white-space: nowrap;
  }
  .wordmark__dot { border-radius: 50%; background: var(--gold); flex: none; }
  .card--front .wordmark { top: 112px; font-size: 27px; }
  .card--front .wordmark__dot { width: 16px; height: 16px; }
  .card--back .wordmark { top: 86px; font-size: 22px; }
  .card--back .wordmark__dot { width: 13px; height: 13px; }

  .owner { position: absolute; left: 114px; top: 160px; font-size: 14px; line-height: 18px; letter-spacing: 0.03em; }
  .owner__role { color: var(--muted); }
  .owner__name { color: var(--ink); }

  .contact { position: absolute; left: 269px; top: 158px; list-style: none; font-size: 13.5px; line-height: 19px; color: var(--muted); }
  .contact li:first-child { font-size: 14.5px; }

  .address { position: absolute; left: 0; right: 0; top: 246px; text-align: center; font-size: 14px; line-height: 18px; color: var(--ink); letter-spacing: 0.02em; }
</style>
</head>
<body>
  <section class="card card--front">
    <div class="lattice-border" role="img" aria-label="Black and silver French lattice quatrefoil pattern border"></div>
    <div class="front-panel">
      <div class="wordmark" style="top:112px"><span class="wordmark__dot"></span>MARLOW ATELIER</div>
    </div>
  </section>

  <section class="card card--back">
    <div class="wordmark"><span class="wordmark__dot"></span>MARLOW ATELIER</div>
    <div class="owner">
      <p class="owner__role">Boutique Owner</p>
      <p class="owner__name">Tessa Wrenfield</p>
    </div>
    <ul class="contact">
      <li>02 **** *TBA</li>
      <li>info@marlowatelier.com.au</li>
      <li>Facebook.com/MarlowAtelier</li>
      <li>www.marlowatelier.com.au</li>
    </ul>
    <p class="address">41B Parrin Lane Calloway Cove NSW 2093<br>Australia 0471239046</p>
  </section>
</body>
</html>
```